Creative Swimming Pool Facebook Design

We need A creative Facebook Page for a swimming pool company named "Wavecrest Pools" using our logo. Our slogan is "better service for a better price." the design should have a Connecticut feel to it (not tropics).

Industry/Entity Type

It Company

Font styles to use
Serif
Sans Serif

```html
<!DOCTYPE html>
<html lang="en">
<head>
<meta charset="utf-8">
<title>Wavecrest Pools – Page</title>
<link href="https://fonts.googleapis.com/css2?family=Arimo:ital,wght@0,400;0,700;1,400&family=Libre+Baskerville:ital@1&display=swap" rel="stylesheet">
<style>
:root{
  --bar-blue:#4b64a0;
  --bar-blue-dark:#3b5998;
  --notice-blue:#6f83b4;
  --link-blue:#3b5998;
  --bg:#e9ebee;
  --card:#ffffff;
  --line:#dddfe2;
  --text:#1d2129;
  --muted:#90949c;
  --soft:#f6f7f9;
  --placeholder:#c8d0e0;
  --sea-top:#8ec9e8;
  --sea-mid:#4f9fcc;
  --sea-deep:#22689a;
  --brand:#1f7fc4;
  --post-btn:#4c67a1;
}
*{box-sizing:border-box;margin:0;padding:0}
html,body{width:1200px;height:893px;overflow:hidden;background:var(--bg)}
body{font-family:Arimo,Arial,sans-serif;color:var(--text)}
.stage{position:relative;width:1122px;height:835px;transform:scale(1.06952);transform-origin:0 0}
.abs{position:absolute}

.topbar{left:0;top:0;width:1122px;height:43px;background:linear-gradient(var(--bar-blue),var(--bar-blue-dark));border-bottom:1px solid #29487d}
.topbar .mark{left:75px;top:9px;width:22px;height:22px;background:#fff;border-radius:2px}
.topbar .search{left:105px;top:9px;width:400px;height:24px;background:#fff;border-radius:2px;font-size:14px;color:#777;padding:4px 7px}
.topbar .search svg{position:absolute;right:7px;top:5px}
.notice{left:0;top:43px;width:1122px;height:27px;background:var(--notice-blue);color:#fff;font-size:12px;text-align:center;line-height:27px}

.pagenav{left:76px;top:70px;width:983px;height:45px;background:var(--card);border:1px solid var(--line);border-top:0;font-size:14px}
.pagenav .item{position:absolute;top:0;height:45px;line-height:45px;color:#4b4f56}
.pagenav .item.active{font-weight:700;color:var(--text);border-bottom:3px solid var(--post-btn)}
.pagenav .sep{position:absolute;top:10px;width:1px;height:26px;background:var(--line)}

.cover-card{left:75px;top:124px;width:850px;height:358px;background:var(--card);border:1px solid var(--line)}
.cover{left:0;top:0;width:850px;height:314px;background:linear-gradient(180deg,#b6dcf0 0%,var(--sea-top) 25%,var(--sea-mid) 55%,var(--sea-deep) 100%)}
.slogan{left:128px;top:86px;font-family:"Libre Baskerville",Georgia,serif;font-style:italic;font-size:25px;color:#fff;text-shadow:0 1px 3px rgba(0,0,0,.35)}
.page-name{left:194px;top:246px;color:#fff;font-size:23px;font-weight:700;text-shadow:0 1px 3px rgba(0,0,0,.5)}
.page-cat{left:194px;top:278px;color:#fff;font-size:17px;text-shadow:0 1px 3px rgba(0,0,0,.5)}
.btn{position:absolute;height:27px;background:#f6f7f9;border:1px solid #ccd0d5;border-radius:2px;font-size:12px;font-weight:700;color:#4b4f56;line-height:25px;display:flex;align-items:center;gap:5px;padding:0 8px}
.btn-group{left:620px;top:276px;width:218px;height:27px;background:#f6f7f9;border:1px solid #ccd0d5;border-radius:2px;display:flex}
.btn-group span{display:flex;align-items:center;gap:5px;padding:0 8px;font-size:12px;font-weight:700;color:#4b4f56;border-right:1px solid #ccd0d5}
.btn-group span:last-child{border:0;flex:1;justify-content:center}
.profile{left:14px;top:176px;width:169px;height:170px;background:#fff;border:1px solid #bec2c9;border-radius:3px;display:flex;align-items:center;justify-content:center;gap:6px}
.profile .dot{width:12px;height:12px;border-radius:50%;background:var(--brand)}
.profile .brand{font-size:15px;font-weight:700;color:var(--brand)}
.tabs{left:185px;top:314px;height:44px;font-size:14px}
.tabs .tab{position:absolute;top:0;height:44px;line-height:44px;color:#4b4f56;white-space:nowrap}
.tabs .tab.active{font-weight:700;color:var(--text);border-bottom:3px solid var(--post-btn)}
.tabs .sep{position:absolute;top:10px;width:1px;height:24px;background:var(--line)}

.stats{left:937px;top:124px;width:122px;height:292px;background:var(--card);border:1px solid var(--line);text-align:center}
.stats .head{height:37px;line-height:37px;font-size:12px;font-weight:700;background:var(--soft);border-bottom:1px solid var(--line)}
.stats .stat{margin:0 10px;height:54px;padding-top:14px;border-bottom:1px solid var(--line)}
.stats .stat:last-child{border:0}
.stats .num{font-size:13px;font-weight:700}
.stats .lbl{font-size:11px;color:var(--link-blue)}
.stats .stat.plain .lbl{color:#4b4f56}

.years{left:937px;top:437px;font-size:12px;color:var(--muted);border-left:4px solid #d3d6db}
.years div{height:24.3px;padding-left:6px;line-height:24px}
.years .current{font-weight:700;color:#7f8289;border-left:4px solid #5a5f68;margin-left:-4px;padding-left:6px}

.people{left:76px;top:493px;width:327px;height:312px;background:var(--card);border:1px solid var(--line)}
.people .head{height:38px;padding:0 10px;font-size:11px;font-weight:700;color:#4b4f56;display:flex;justify-content:space-between;align-items:center;background:var(--soft);border-bottom:1px solid var(--line)}
.people .likes{height:44px;text-align:center;line-height:44px;font-size:14px;color:var(--muted);border-bottom:1px solid var(--line);margin:0 0}
.people .likes b{color:var(--text)}
.people .friends{position:absolute;left:13px;top:96px;font-size:12px;color:#4b4f56}
.people a{color:var(--link-blue);font-weight:700;text-decoration:none}
.avatar{position:absolute;background:var(--placeholder);overflow:hidden}
.avatar svg{display:block}
.more{position:absolute;left:262px;top:122px;width:45px;height:45px;background:#ebeef4;color:#7b8bb2;font-size:17px;font-weight:700;text-align:center;line-height:45px}
.invite-row{position:absolute;left:12px;font-size:12px}
.invite-row .name{position:absolute;left:48px;top:13px;color:var(--link-blue);font-weight:700;white-space:nowrap}
.invite{position:absolute;left:267px;top:9px;height:23px;padding:0 7px;border:1px solid #ccd0d5;background:#f6f7f9;border-radius:2px;font-size:12px;font-weight:700;color:#4b4f56;line-height:21px}
.see-all{position:absolute;left:13px;top:286px;font-size:12px;color:var(--link-blue)}

.composer{left:415px;top:493px;width:510px;height:312px;background:var(--card);border:1px solid var(--line)}
.composer .modes{height:36px;display:flex;align-items:center;gap:14px;padding-left:12px;font-size:12px;font-weight:700;color:#4b4f56;border-bottom:1px solid var(--line)}
.composer .modes span{display:flex;align-items:center;gap:6px}
.composer .body{position:absolute;left:64px;top:49px;width:436px;font-size:13.3px;line-height:18.1px;height:217px;overflow:hidden}
.composer .foot{position:absolute;left:0;bottom:0;width:508px;height:42px;background:var(--soft);border-top:1px solid var(--line)}
.boost{position:absolute;left:332px;top:8px;width:94px;height:26px;border:1px solid #ccd0d5;background:#f6f7f9;border-radius:2px;font-size:12px;font-weight:700;color:#4b4f56;line-height:24px;text-align:center}
.post{position:absolute;left:441px;top:8px;width:61px;height:26px;background:var(--post-btn);border-radius:2px;color:#fff;font-size:12px;font-weight:700;text-align:center;line-height:26px}
</style>
</head>
<body>
<div class="stage">

  <header class="topbar abs">
    <div class="mark abs"></div>
    <div class="search abs">Search for people, places and things
      <svg width="13" height="13" viewBox="0 0 13 13"><circle cx="5.5" cy="5.5" r="4.2" fill="none" stroke="#9197a3" stroke-width="1.6"/><line x1="8.6" y1="8.6" x2="12" y2="12" stroke="#9197a3" stroke-width="1.8"/></svg>
    </div>
  </header>
  <div class="notice abs">You are posting, commenting and liking as <b>Your Page Name</b> — Change to Personal Profile</div>

  <nav class="pagenav abs">
    <span class="item active" style="left:15px">Page</span>
    <span class="sep" style="left:67px"></span>
    <span class="item" style="left:83px">Activity</span>
    <span class="sep" style="left:144px"></span>
    <span class="item" style="left:161px">Insights</span>
    <span class="sep" style="left:228px"></span>
    <span class="item" style="left:244px">Settings</span>
    <span class="sep" style="left:762px"></span>
    <span class="item" style="left:780px">Build Audience ▾</span>
    <span class="sep" style="left:905px"></span>
    <span class="item" style="left:922px">Help ▾</span>
  </nav>

  <section class="cover-card abs">
    <div class="cover abs" role="img" aria-label="Cover photo: a swimmer resting on the edge of an infinity pool overlooking calm sea and distant islands"></div>
    <div class="slogan abs">“better service for a better price”</div>
    <div class="page-name abs">WAVECREST POOLS</div>
    <div class="page-cat abs">Swimming Pool Company</div>
    <div class="btn" style="left:525px;top:276px;width:84px">
      <svg width="12" height="12" viewBox="0 0 12 12"><path d="M1 5h2.5v6H1zM4.5 11V5l2.5-4c1 0 1.3.8 1 2L7.6 4.5H11l-1 6.5z" fill="#4267b2"/></svg>Liked ▾
    </div>
    <div class="btn-group abs">
      <span><svg width="12" height="10" viewBox="0 0 12 10"><path d="M1 5l3.5 3.5L11 1.5" fill="none" stroke="#4b4f56" stroke-width="2"/></svg>Following</span>
      <span><svg width="12" height="11" viewBox="0 0 12 11"><path d="M1 1h10v7H5l-3 2.5V8H1z" fill="#4b4f56"/></svg>Message</span>
      <span style="font-size:16px;letter-spacing:1px">•••</span>
    </div>
    <div class="profile abs"><span class="dot"></span><span class="brand">Wavecrest Pools</span></div>
    <div class="tabs abs">
      <span class="tab active" style="left:15px">Timeline</span>
      <span class="sep" style="left:88px"></span>
      <span class="tab" style="left:107px">About</span>
      <span class="sep" style="left:161px"></span>
      <span class="tab" style="left:177px">Photos</span>
      <span class="sep" style="left:238px"></span>
      <span class="tab" style="left:254px">Likes</span>
      <span class="sep" style="left:304px"></span>
      <span class="tab" style="left:320px">More ▾</span>
    </div>
  </section>

  <aside class="stats abs">
    <div class="head">THIS WEEK</div>
    <div class="stat"><div class="num">999</div><div class="lbl">Page Likes</div></div>
    <div class="stat plain"><div class="num">999</div><div class="lbl">Post <span style="color:var(--link-blue)">Reach</span></div></div>
    <div class="head" style="border-top:1px solid var(--line)">UNREAD</div>
    <div class="stat"><div class="num">999</div><div class="lbl">Notifications</div></div>
    <div class="stat"><div class="num">999</div><div class="lbl">Messages</div></div>
  </aside>

  <div class="years abs">
    <div class="current">Recent</div>
    <div>2013</div>
    <div>2012</div>
    <div>2011</div>
    <div>2010</div>
  </div>

  <section class="people abs">
    <div class="head">PEOPLE<svg width="9" height="13" viewBox="0 0 9 13"><path d="M2 1.5l5 5-5 5" fill="none" stroke="#4b4f56" stroke-width="2"/></svg></div>
    <div class="likes"><b>999</b> likes</div>
    <div class="friends"><a>Example person</a>, and <a>99 others</a> like this.</div>
    <div class="avatar" style="left:12px;top:122px;width:45px;height:45px"><svg width="45" height="45" viewBox="0 0 45 45"><circle cx="22.5" cy="17" r="9" fill="#fff"/><path d="M5 45c1-12 9-15 17.5-15S39 33 40 45z" fill="#fff"/></svg></div>
    <div class="avatar" style="left:62px;top:122px;width:45px;height:45px"><svg width="45" height="45" viewBox="0 0 45 45"><circle cx="22.5" cy="17" r="9" fill="#fff"/><path d="M5 45c1-12 9-15 17.5-15S39 33 40 45z" fill="#fff"/></svg></div>
    <div class="avatar" style="left:112px;top:122px;width:45px;height:45px"><svg width="45" height="45" viewBox="0 0 45 45"><circle cx="22.5" cy="17" r="9" fill="#fff"/><path d="M5 45c1-12 9-15 17.5-15S39 33 40 45z" fill="#fff"/></svg></div>
    <div class="avatar" style="left:162px;top:122px;width:45px;height:45px"><svg width="45" height="45" viewBox="0 0 45 45"><circle cx="22.5" cy="17" r="9" fill="#fff"/><path d="M5 45c1-12 9-15 17.5-15S39 33 40 45z" fill="#fff"/></svg></div>
    <div class="avatar" style="left:212px;top:122px;width:45px;height:45px"><svg width="45" height="45" viewBox="0 0 45 45"><circle cx="22.5" cy="17" r="9" fill="#fff"/><path d="M5 45c1-12 9-15 17.5-15S39 33 40 45z" fill="#fff"/></svg></div>
    <div class="more">+99</div>
    <div class="invite-row" style="top:178px">
      <div class="avatar" style="left:0;top:0;width:40px;height:40px"><svg width="40" height="40" viewBox="0 0 45 45"><circle cx="22.5" cy="17" r="9" fill="#fff"/><path d="M5 45c1-12 9-15 17.5-15S39 33 40 45z" fill="#fff"/></svg></div>
      <span class="name">Example person</span><span class="invite">Invite</span>
    </div>
    <div class="invite-row" style="top:229px">
      <div class="avatar" style="left:0;top:0;width:40px;height:40px"><svg width="40" height="40" viewBox="0 0 45 45"><circle cx="22.5" cy="17" r="9" fill="#fff"/><path d="M5 45c1-12 9-15 17.5-15S39 33 40 45z" fill="#fff"/></svg></div>
      <span class="name">Example person</span><span class="invite">Invite</span>
    </div>
    <div class="see-all">See All Friends</div>
  </section>

  <section class="composer abs">
    <div class="modes">
      <span><svg width="15" height="15" viewBox="0 0 15 15"><rect width="15" height="15" rx="2" fill="#4a77c4"/><path d="M4 11l1-3 5-5 2 2-5 5z" fill="#fff"/></svg>Status</span>
      <span><svg width="15" height="15" viewBox="0 0 15 15"><rect x=".5" y=".5" width="14" height="14" rx="2" fill="#fbe3c9" stroke="#e8822f"/><rect x="3.5" y="3.5" width="8" height="8" fill="none" stroke="#e8822f"/></svg>Photo / Video</span>
      <span><svg width="15" height="15" viewBox="0 0 15 15"><rect x=".5" y=".5" width="14" height="14" rx="1" fill="#fff" stroke="#7a7f87"/><rect x=".5" y=".5" width="14" height="3" fill="#c0392b"/><text x="7.5" y="12.5" font-size="7" text-anchor="middle" fill="#333" font-family="Arimo,sans-serif">31</text></svg>Event, Milestone +</span>
    </div>
    <div class="avatar" style="left:11px;top:49px;width:42px;height:42px"><svg width="42" height="42" viewBox="0 0 45 45"><circle cx="22.5" cy="17" r="9" fill="#fff"/><path d="M5 45c1-12 9-15 17.5-15S39 33 40 45z" fill="#fff"/></svg></div>
    <p class="body">Lorem ipsum dolor sit amet, consectetur adipiscing elit. Etiam sit amet ante nisi, sit amet fermentum erat. Suspendisse vel nunc a massa consequat iaculis. Sed pellentesque vehicula elit. Mauris sodales mollis molestie. Integer ultrices laoreet ante, et faucibus sem cursus non. Suspendisse laoreet suscipit vestibulum. Integer mi augue, hendrerit ut fermentum ut, accumsan eget justo. Nam fringilla dapibus risus sed consequat. Nullam lacus urna, pellentesque et laoreet sit amet, volutpat sit amet dolor. Praesent a ultrices velit. Nulla facilisi. Ut sagittis dapibus bibendum. Proin id enim eros. Curabitur tincidunt lorem sed purus semper vitae tincidunt purus aliquet. Integer nulla metus, vestibulum at tincidunt at, euismod sed ligula. Vestibulum ante ipsum primis in faucibus orci</p>
    <div class="foot">
      <svg class="abs" style="left:12px;top:13px" width="16" height="16" viewBox="0 0 16 16"><circle cx="8" cy="8" r="6.8" fill="none" stroke="#90949c" stroke-width="1.6"/><path d="M8 4v4.5h3" fill="none" stroke="#90949c" stroke-width="1.6"/></svg>
      <svg class="abs" style="left:53px;top:12px" width="13" height="17" viewBox="0 0 13 17"><path d="M6.5 16S1 9.5 1 6.2a5.5 5.5 0 0111 0C12 9.5 6.5 16 6.5 16z" fill="#90949c"/><circle cx="6.5" cy="6" r="2" fill="#f6f7f9"/></svg>
      <svg class="abs" style="left:91px;top:13px" width="17" height="15" viewBox="0 0 17 15"><path d="M1 4h4l1.5-2.5h4L12 4h4v10H1z" fill="#90949c"/><circle cx="8.5" cy="8.5" r="3" fill="#f6f7f9"/></svg>
      <div class="boost">Boost Post ▾</div>
      <div class="post">Post</div>
    </div>
  </section>

</div>
</body>
</html>
```